Brochure Design Project

Using supplied logo and supplied graphics I want a 4-page brochure 81/2x 11" that can be used as a leave behind, a self mailer and a pdf email attachment for promotion purposes.
The cover needs to be visually provocative and support the following questions"
"Have you lost your leadership edge... has your company lost it's momentum... are your employees as engaged as they need to be?"
The inside of the brochure should explain the Amber Ridge Coaching 7 Step process with is explained in the attached PowerPoint.
Back page should be brief bio of me. And Statement about who we work with. I am attaching a tri-fold brochure we designed but do not like because it is bland and the graphic inside is hard to read.
Target Market(s)
"C" level executives (CEO, CIO, CFO, CMO, CRO etc)
Industry/Entity Type
Leadership
Look and feel

```html
<!DOCTYPE html>
<html lang="en">
<head>
<meta charset="utf-8">
<title>Amber Ridge Coaching — Brochure</title>
<link rel="stylesheet" href="https://fonts.googleapis.com/css2?family=Libre+Bodoni:wght@700&family=Questrial&family=Open+Sans:ital,wght@0,400;0,600;0,700;1,600;1,700&display=swap">
<style>
:root{
  --slate:#5f7591;
  --slate-dark:#4d6682;
  --navy:#2f4862;
  --sage:#7e8b6f;
  --olive:#7f9a45;
  --lime:#9cb53a;
  --mist:#dcdde0;
  --mist-light:#e8e9ea;
  --stone:#c9ccd0;
  --ink:#4a4f55;
  --white:#ffffff;
}
*{box-sizing:border-box;margin:0;padding:0}
html,body{width:1200px;height:376px;overflow:hidden;background:var(--white)}
body{position:relative;font-family:"Open Sans",Arial,sans-serif;color:var(--ink)}
/* Sheet is laid out at double size and scaled down so fine print renders crisply */
.sheet{position:absolute;left:0;top:0;width:2400px;height:752px;transform:scale(.5);transform-origin:0 0}
.panel{position:absolute;top:0;height:728px;overflow:hidden}
.fill{position:absolute}
.small{font-size:8.4px;line-height:1.45}

/* Cover */
.cover{left:0;width:554px;background:var(--stone)}
.cover-photo{left:0;top:0;width:554px;height:444px;background:linear-gradient(180deg,#8e99a6 0%,#6f7d8c 45%,#3e4652 100%)}
.cover-title{position:absolute;left:76px;top:52px;font-family:"Libre Bodoni",Georgia,serif;font-weight:700;color:var(--white);font-size:40px;line-height:1.0}
.cover-lower{left:0;top:444px;width:554px;height:284px;background:#cdd0d3}
.cover-stripe{left:0;top:444px;width:74px;height:284px;background:#b7bbc0}
.logo-box{position:absolute;left:90px;top:536px;width:164px;height:72px;background:var(--white);display:flex;align-items:center;justify-content:center;gap:6px}
.logo-box .dot{width:12px;height:12px;border-radius:50%;background:var(--slate)}
.logo-box .name{font-weight:700;font-size:12.4px;color:var(--slate-dark)}
.cover-address{position:absolute;left:90px;top:618px;color:var(--white);font-size:7.6px;line-height:1.55;font-style:normal}
.cover-subtitle{position:absolute;left:284px;top:546px;font-family:"Libre Bodoni",Georgia,serif;font-weight:700;color:var(--olive);font-size:28px;line-height:1.05}

/* Inside left: process */
.process{left:586px;width:570px;background:var(--white)}
.steps-area{left:0;top:0;width:314px;height:470px;background:var(--mist)}
.step-circle{position:absolute;left:16px;width:80px;height:80px;border-radius:50%;display:flex;align-items:center;justify-content:center;font-family:"Questrial",Arial,sans-serif;font-size:24px}
.step-circle.dark{background:var(--navy);color:var(--mist-light)}
.step-circle.light{background:#eceded;color:var(--navy)}
.step-circle.final{background:var(--sage);color:var(--white);width:92px;height:92px;left:10px;font-size:22px}
.step-list{position:absolute;left:112px;top:40px;width:194px}
.step-list h4{font-size:8.8px;font-weight:700;color:var(--lime);margin-top:3px}
.step-list p{font-size:8.2px;line-height:1.4;color:var(--ink)}
.quote-col{left:314px;top:0;width:256px;height:728px;background:var(--slate)}
.quote{position:absolute;left:328px;top:14px;width:232px;font-style:italic;font-weight:700;color:var(--white);font-size:15.6px;line-height:1.26}
.quote-mark{font-family:"Libre Bodoni",Georgia,serif;color:#9fb0c4;font-size:26px;line-height:0}
.quote-cite{position:absolute;left:332px;top:326px;color:#dde3ea;font-size:8.2px;line-height:1.4}
.bio-photo{left:334px;top:390px;width:212px;height:210px;background:linear-gradient(160deg,#8d98a3,#6a7582);border:6px solid #d7dce2}
.bio{position:absolute;left:330px;top:610px;width:222px;color:var(--white);font-size:8.2px;line-height:1.5;font-weight:600}
.process-head{position:absolute;left:36px;top:482px;font-family:"Questrial",Arial,sans-serif;color:var(--slate-dark);font-size:38px;font-weight:400}
.process-kicker{position:absolute;left:36px;top:526px;font-size:9px;font-weight:700;color:var(--sage)}
.process-body{position:absolute;left:36px;top:544px;width:266px}
.process-body p{margin-bottom:6px}
.process-body .lead{font-style:italic;color:#8d939a}

/* Inside right: promise */
.promise{left:1156px;width:580px;background:var(--white)}
.promise-head{position:absolute;left:34px;top:34px;font-family:"Questrial",Arial,sans-serif;color:var(--slate-dark);font-size:44px;font-weight:400}
.promise-kicker{position:absolute;left:36px;top:88px;font-size:9.4px;font-weight:700;color:var(--sage)}
.promise-body{position:absolute;left:36px;top:108px;width:526px}
.chalk-photo{left:34px;top:244px;width:292px;height:212px;background:linear-gradient(135deg,#3c3f43,#6a6d71 60%,#4b4e52)}
.stat-box{left:326px;top:226px;width:240px;height:230px;background:var(--sage)}
.stat-number{position:absolute;left:344px;top:234px;font-family:"Questrial",Arial,sans-serif;color:var(--white);font-size:62px;font-weight:700}
.stat-text{position:absolute;left:344px;top:326px;width:208px;color:var(--white);font-size:9px;line-height:1.5;font-weight:600}
.program-head{position:absolute;left:36px;top:482px;width:300px;font-size:10px;font-weight:700;color:var(--slate-dark);line-height:1.4}
.program-list{position:absolute;left:36px;top:532px;width:330px;list-style:none}
.program-list li{position:relative;padding-left:18px;margin-bottom:3px}
.program-list li::before{content:"»";position:absolute;left:0;top:-1px;color:var(--sage);font-size:10px}
.ladder-photo{left:380px;top:496px;width:150px;height:140px;background:linear-gradient(180deg,#f2f2f2,#d6d8da);border:4px solid #e1e3e5;box-shadow:0 0 0 2px #c8ccd0}

/* Back */
.back{left:1760px;width:640px;background:var(--mist-light)}
.back-band{left:0;top:0;width:640px;height:150px;background:var(--slate)}
.back-tagline{position:absolute;left:52px;top:82px;font-family:"Questrial",Arial,sans-serif;color:#dfe5ec;font-size:16px}
.back-photo{left:0;top:150px;width:536px;height:250px;background:linear-gradient(135deg,#42464b,#6e7276 55%,#505459)}
.back-accent{left:536px;top:150px;width:104px;height:250px;background:var(--sage)}
.back-block-a{left:0;top:400px;width:330px;height:92px;background:var(--slate-dark)}
.back-block-b{left:330px;top:400px;width:310px;height:92px;background:var(--slate)}
.back-contact{position:absolute;left:38px;top:522px;font-size:7.8px;line-height:1.55;color:var(--ink);font-style:normal}
.back-contact .name{display:flex;align-items:center;gap:4px;font-weight:700;font-size:9px;color:var(--slate-dark)}
.back-contact .dot{width:8px;height:8px;border-radius:50%;background:var(--slate)}
.postage{position:absolute;left:470px;top:520px;width:104px;height:60px;background:var(--white);border:1px solid #8b9096;font-size:7.2px;line-height:1.5;text-align:center;padding-top:12px;color:var(--ink)}
</style>
</head>
<body>
<div class="sheet">

<!-- Cover -->
<section class="panel cover">
  <div class="fill cover-photo" role="img" aria-label="Group photo of business executives in suits"></div>
  <h1 class="cover-title">Regain<br>Your<br>Competitive<br>Edge</h1>
  <div class="fill cover-lower"></div>
  <div class="fill cover-stripe"></div>
  <div class="logo-box"><span class="dot"></span><span class="name">Amber Ridge Coaching</span></div>
  <address class="cover-address">48 Larkspur Lane<br>Suite 210<br>Fairview, OR 97024<br>www.amberridgecoaching.com</address>
  <h2 class="cover-subtitle">Executive and<br>Organizational<br>Coaching</h2>
</section>

<!-- Inside left: process -->
<section class="panel process">
  <div class="fill steps-area"></div>
  <div class="step-circle dark" style="top:28px">ONE</div>
  <div class="step-circle light" style="top:84px">TWO</div>
  <div class="step-circle dark" style="top:140px">THREE</div>
  <div class="step-circle light" style="top:196px">FOUR</div>
  <div class="step-circle dark" style="top:252px">FIVE</div>
  <div class="step-circle light" style="top:308px">SIX</div>
  <div class="step-circle final" style="top:362px">SEVEN</div>
  <div class="step-list">
    <h4>Create a Safety Net.</h4>
    <p>We'll help your organization face change by exposing the benefits and challenges the fears behind it.</p>
    <h4>Identify the Problem.</h4>
    <p>The next step is to evaluate the situation. We'll look at individual and management using the CLI assessment tool.</p>
    <h4>Dive Deep.</h4>
    <p>Using Hierarchy Methodology, we'll map the beliefs and processes that created the crisis.</p>
    <h4>Consensus March.</h4>
    <p>Achieve a common view of the problem and create the path for alignment toward a new vision for the organization.</p>
    <h4>SWOT Analysis.</h4>
    <p>We'll conduct both a SWOT and a Block Analysis to determine strengths and potential obstacles to success.</p>
    <h4>Set Goals.</h4>
    <p>We'll conduct goal-setting and attainment planning using the AIM SMART process.</p>
    <h4>Meet the Master.</h4>
    <p>The meat of the process is intensive coaching on dismantling obstacles, meeting challenges and achieving the goals you articulate.</p>
  </div>

  <div class="fill quote-col"></div>
  <p class="quote"><span class="quote-mark">“</span>Whether your organization's diagnosis is mild dysfunction or complete disengagement, our job is to help you pivot. That is, find the turning point that helps you to take your pulse, regain control, breathe again and get back on the path to achieving growth.<span class="quote-mark">”</span></p>
  <p class="quote-cite">Daniel R. Whitcombe, CEO<br>Amber Ridge Coaching</p>
  <div class="fill bio-photo" role="img" aria-label="Portrait photo of the company founder"></div>
  <p class="bio">After 30-years as a senior executive in the print and online business-to-business media business Daniel founded Amber Ridge Coaching to apply his skill and experience to help individuals and organizations facing "must change" situations. He lives in Oregon with his wife and three children.</p>

  <h2 class="process-head">Our Process</h2>
  <p class="process-kicker">From Distress to Success</p>
  <div class="process-body small">
    <p class="lead">Amber Ridge Coaching provides one-on-one and group coaching focused on enabling individuals and organizations to align their values, strengths and goals to achieve extraordinary, sustainable outcomes even in the most challenging situations.</p>
    <p>Amber Ridge Coaching services include up to five individual CLI Assessments, with one-hour, one-on-one debriefings conducted by CLI Master Practitioners. In addition, you'll receive five, one-hour situation analysis interviews with your senior management team and up to 10 hours of interviews with other stakeholders. We provide comprehensive Mind Mapping, with visual representation of the results of the interviews. We present two, five-hour management group sessions to present findings and to set goals. Finally the mentoring service includes 26 one-hour coaching sessions with each of your senior executives.</p>
  </div>
</section>

<!-- Inside right: promise -->
<section class="panel promise">
  <h2 class="promise-head">Our Promise</h2>
  <p class="promise-kicker">Coaching Helps Inspire Individuals Toward Positive and Sustainable Action.</p>
  <p class="promise-body small">Amber Ridge Coaching works with executives and companies that are facing issues ranging from mild dysfunction to significant distress. We help them gain regain control and achieve renewed growth. Amber Ridge Coaching employs the Core Leadership process developed by Marcus T. Ellery PhD, founder of the Harlan Institute for Leadership Coaching (HILC). Core Leadership is the process that develops a personally effective style of leadership that positively influences and changes not only the leader, but also those with whom they work and interact, as well as their organization as a whole.</p>
  <div class="fill chalk-photo" role="img" aria-label="Photo of a man writing equations on a chalkboard"></div>
  <div class="fill stat-box"></div>
  <p class="stat-number">79%</p>
  <p class="stat-text">Of the thousands of companies that use some form of coaching, the vast majority use it to improve performance, according to the National Management Council 2008 Coaching Survey.</p>
  <p class="program-head">The Amber Ridge Coaching Program is a 7-step process that results in:</p>
  <ul class="program-list small">
    <li>Fearless, confident leaders who share understanding of the organization's situation</li>
    <li>Appreciation for what motivates each management team member — eliminating hidden agendas and second-guessing</li>
    <li>Trust, respect and cooperation among management team members, focused on what brings results and moving through the "blocks" that impede progress</li>
    <li>Clearly articulated goals, measurements of success and durable confidence across the organization</li>
    <li>A success environment where everyone feels capable of meeting any challenge and exploring every opportunity</li>
  </ul>
  <div class="fill ladder-photo" role="img" aria-label="Sketch of a man climbing a ladder toward a chalkboard"></div>
</section>

<!-- Back -->
<section class="panel back">
  <div class="fill back-band"></div>
  <p class="back-tagline">Get Back on Track.</p>
  <div class="fill back-photo" role="img" aria-label="Photo of a man on a ladder at a chalkboard wall"></div>
  <div class="fill back-accent"></div>
  <div class="fill back-block-a"></div>
  <div class="fill back-block-b"></div>
  <address class="back-contact">
    <span class="name"><span class="dot"></span>Amber Ridge Coaching</span>
    48 Larkspur Lane<br>Suite 210<br>Fairview, OR 97024<br>T: (503) 555-0147<br>F: (503) 555-0183<br>www.amberridgecoaching.com
  </address>
  <div class="postage">US POSTAGE PAID<br>FAIRVIEW, OR<br>PERMIT NO. 104<br>ZIP CODE 97024</div>
</section>

</div>
</body>
</html>
```